New business card with our logo

we finalized our logo with the help of pixel harbor - now we need a business card using that logo. we are a metal service center providing raw steel and metal products for fabricating, contractors, artists, etc. we have the wording for the back of the card figured out (attached, no deviations from text please), just need help putting it all together.
would like the look of steel somehow incorporated in the design ... would like the black part of the logo to be steel or silver color (the S & BRANLEY)
Other font styles liked:
- calibri, arial, similar to those, modern looking
Colors
Designer to choose colors to be used in the design.
Requirements
Must have
- Back of card must haves are attached (no deviations from wording please).
- FRONT of card:
- logo
- address
- name
- office tel
- cell
- fax
- website
- address
Nice to have
- incorporate the look of steel or element of steel somehow
- names of the staff on front not in all caps, i.e. Rosvita not ROSVITA
- this industry is more industrial, not coffee or flower shop so design should be aligned with that
- design should be classic and tasteful

```html
<!DOCTYPE html>
<html lang="en">
<head>
<meta charset="utf-8">
<title>Branley Steel – Business Card</title>
<link href="https://fonts.googleapis.com/css2?family=Montserrat:wght@400;500;600;700&family=Roboto:wght@400;500&family=Work+Sans:wght@400&display=swap" rel="stylesheet">
<style>
  :root {
    --stage: #6b6b6b;
    --card: #1b1b1b;
    --card-edge: #9a9a9a;
    --silver: #c9c9c9;
    --silver-soft: #a8a8a8;
    --silver-dim: #8a8a8a;
    --rule: #7a7a7a;
  }
  * { margin: 0; padding: 0; box-sizing: border-box; }
  html, body { width: 1200px; height: 900px; overflow: hidden; }
  body {
    background: var(--stage);
    position: relative;
    font-family: "Montserrat", sans-serif;
  }
  .card {
    position: absolute;
    width: 640px;
    height: 366px;
    background: var(--card);
    border: 1px solid var(--card-edge);
    box-shadow: 0 10px 24px rgba(0,0,0,.45);
    color: var(--silver);
  }
  .card-back { left: 460px; top: 56px; }
  .card-front { left: 100px; top: 476px; }

  .brand {
    display: flex;
    align-items: center;
    gap: 12px;
  }
  .brand-dot {
    border: 3px solid var(--silver);
    border-radius: 50%;
  }
  .brand-name {
    font-family: "Montserrat", sans-serif;
    font-weight: 700;
    color: var(--silver);
    letter-spacing: .5px;
  }

  /* back */
  .card-back .content {
    position: absolute;
    left: 0; right: 0; top: 44px;
    display: flex;
    flex-direction: column;
    align-items: center;
    text-align: center;
  }
  .card-back .brand-dot { width: 58px; height: 58px; }
  .card-back .brand-name { font-size: 34px; }
  .service-title {
    margin-top: 26px;
    font-size: 24px;
    font-weight: 600;
    letter-spacing: 1px;
  }
  .service-list {
    margin-top: 4px;
    font-size: 15px;
    font-weight: 400;
    letter-spacing: 1.5px;
    color: var(--silver-soft);
  }
  .back-rule {
    width: 330px;
    height: 1px;
    background: var(--rule);
    margin: 16px 0 12px;
  }
  .product-line {
    font-size: 13px;
    font-weight: 500;
    color: var(--silver-dim);
    line-height: 1.6;
  }
  .tagline {
    margin-top: 14px;
    font-size: 16px;
    font-weight: 500;
    color: var(--silver);
  }

  /* front */
  .card-front .brand {
    position: absolute;
    right: 48px;
    top: 36px;
  }
  .card-front .brand-dot { width: 50px; height: 50px; }
  .card-front .brand-name { font-size: 28px; }
  .person {
    position: absolute;
    left: 36px;
    top: 108px;
  }
  .person-name {
    font-family: "Roboto", sans-serif;
    font-weight: 500;
    font-size: 30px;
    color: var(--silver);
  }
  .person-role {
    font-family: "Roboto", sans-serif;
    font-size: 15px;
    color: var(--silver-dim);
  }
  .front-rule {
    position: absolute;
    left: 36px;
    right: 40px;
    top: 190px;
    height: 1px;
    background: var(--rule);
  }
  .contacts {
    position: absolute;
    left: 40px;
    top: 212px;
    list-style: none;
    font-family: "Work Sans", sans-serif;
    font-size: 17px;
    color: var(--silver-soft);
    line-height: 24px;
  }
  .contacts li { display: flex; align-items: center; gap: 12px; }
  .contacts svg { width: 13px; height: 13px; flex: none; }
  .address {
    position: absolute;
    right: 40px;
    bottom: 32px;
    text-align: right;
    font-family: "Work Sans", sans-serif;
    font-size: 17px;
    line-height: 26px;
    color: var(--silver-soft);
    font-style: normal;
  }
</style>
</head>
<body>

<section class="card card-back" aria-label="Card back">
  <div class="content">
    <div class="brand">
      <span class="brand-dot"></span>
      <span class="brand-name">BRANLEY STEEL</span>
    </div>
    <h2 class="service-title">METAL SERVICE CENTER</h2>
    <p class="service-list">CUT - SHEAR - PUNCH - LIGHT FAB</p>
    <div class="back-rule"></div>
    <p class="product-line">Structural Steel - Stainless &amp; aluminn</p>
    <p class="product-line">Building Components - Rebar - Decking ...and more</p>
    <p class="tagline">Cut to size, Pick-up or Delivered!</p>
  </div>
</section>

<section class="card card-front" aria-label="Card front">
  <div class="brand">
    <span class="brand-dot"></span>
    <span class="brand-name">BRANLEY STEEL</span>
  </div>
  <div class="person">
    <h1 class="person-name">Darren Holt</h1>
    <p class="person-role">Director</p>
  </div>
  <div class="front-rule"></div>
  <ul class="contacts">
    <li>
      <svg viewBox="0 0 16 16" aria-hidden="true"><path d="M3 1l3 3-2 2c1 2 3 4 5 5l2-2 3 3-2 2C7 14 2 9 1 3z" fill="var(--silver-dim)"/></svg>
      +330 2418-5530
    </li>
    <li>
      <svg viewBox="0 0 16 16" aria-hidden="true"><rect x="4" y="1" width="8" height="14" rx="1.5" fill="none" stroke="var(--silver-dim)" stroke-width="1.6"/><circle cx="8" cy="12.5" r="1" fill="var(--silver-dim)"/></svg>
      +330 2391-4076
    </li>
    <li>
      <svg viewBox="0 0 16 16" aria-hidden="true"><rect x="4" y="1" width="8" height="5" fill="none" stroke="var(--silver-dim)" stroke-width="1.4"/><rect x="1" y="6" width="14" height="6" rx="1" fill="var(--silver-dim)"/><rect x="4" y="11" width="8" height="4" fill="none" stroke="var(--silver-dim)" stroke-width="1.4"/></svg>
      +330 2573-6142
    </li>
    <li>
      <svg viewBox="0 0 16 16" aria-hidden="true"><rect x="1" y="3" width="14" height="10" fill="none" stroke="var(--silver-dim)" stroke-width="1.5"/><path d="M1 3l7 6 7-6" fill="none" stroke="var(--silver-dim)" stroke-width="1.5"/></svg>
      info@branleysteel.com
    </li>
    <li>
      <svg viewBox="0 0 16 16" aria-hidden="true"><circle cx="8" cy="8" r="6.5" fill="none" stroke="var(--silver-dim)" stroke-width="1.4"/><ellipse cx="8" cy="8" rx="3" ry="6.5" fill="none" stroke="var(--silver-dim)" stroke-width="1.2"/><path d="M1.5 8h13" stroke="var(--silver-dim)" stroke-width="1.2"/></svg>
      www.branleysteel.com
    </li>
  </ul>
  <address class="address">
    517 Alder Ridge Rd.<br>
    Franklin, TN 37064
  </address>
</section>

</body>
</html>
```